clean web design for a recruitment company

We need a web design for a company called 'TORAVI' recruitment. We are a new age recruitment companies that selects people by their true nature, values and what they can bring to the table as a tangible talent. We are all here possessing a certain talent, whatever that could be that the world needs. The final design should communicate professionalism and strongly embedded etiquette we believe in and a branding promise 'Seeing ones true nature'. Our companies values are integrity, giving away to the community, cherishing the sharing of our talent, time and helping one another.

Target Market(s)

Gulf Countries

Industry/Entity Type

It Company

Number of Pages Required

1 page

Font styles to use
Serif

Requirements
Must have
• Clear and readable font, user friendly structure and easy navigation menus.
Nice to have
• Extra sort of ideas on images we may use, tag lines etc. sample sites we love site:https://www.velmorandi.example/
• http://www.tessabrankow.example/
• http://www.pebbleloomcraft.example/idea-gallery/
Should not have
• all sort of colors, big combination of fonts, images with people in the office or people in suits likewise all the typical industry web sites

```html
<!DOCTYPE html>
<html lang="en">
<head>
<meta charset="utf-8">
<title>Toravi Recruitment — What we do?</title>
<link rel="stylesheet" href="https://fonts.googleapis.com/css2?family=Lato:wght@100;300;400;700;900&display=swap">
<style>
  :root {
    --ink: #1f2023;
    --text: #4f5053;
    --muted: #8a8b8d;
    --paper: #ffffff;
    --rule: #2a2a2a;
    --placeholder: #e4e4e6;
    --placeholder-accent: #f9c9d8;
  }
  * { box-sizing: border-box; margin: 0; padding: 0; }
  html, body {
    width: 1200px; height: 904px; overflow: hidden;
    background: var(--paper);
    font-family: "Lato", Arial, sans-serif;
    color: var(--ink);
  }
  .page { position: relative; width: 1200px; height: 904px; }

  .site-header {
    position: absolute; left: 0; top: 0; width: 1200px; height: 104px;
    border-bottom: 1px solid var(--rule);
  }
  .brand {
    position: absolute; left: 30px; top: 18px;
    font-weight: 700; font-size: 46px; letter-spacing: 1px;
    color: var(--ink); text-decoration: none; line-height: 1;
  }
  .main-nav ul { list-style: none; }
  .main-nav li { position: absolute; top: 20px; }
  .main-nav a {
    display: block; color: var(--ink); text-decoration: none;
    font-size: 18px; font-weight: 400; line-height: 52px; white-space: nowrap;
  }
  .main-nav li.is-current a {
    width: 93px; height: 52px; text-align: center;
    border: 4px solid var(--ink); font-weight: 700; line-height: 44px;
  }
  .nav-team { left: 428px; }
  .nav-method { left: 506px; }
  .nav-areas { left: 645px; }
  .nav-clients { left: 801px; }
  .nav-candidates { left: 896px; }
  .nav-group { left: 1020px; }
  .nav-home { left: 320px; }

  .intro-title {
    position: absolute; left: 0; top: 112px; width: 1200px;
    text-align: center; font-weight: 100; font-size: 100px;
    color: #3a3a3c; line-height: 1.1;
  }

  .portrait {
    position: absolute; top: 284px; width: 136px; height: 186px;
    border-radius: 18px; background: var(--placeholder);
  }
  .portrait--one { left: 200px; }
  .portrait--two { left: 424px; }
  .portrait--three { left: 654px; background: var(--placeholder-accent); }
  .portrait--four { left: 868px; }

  .intro-copy {
    position: absolute; left: 256px; top: 527px; width: 686px;
    font-size: 19.5px; font-weight: 300; line-height: 24.5px;
    color: var(--text);
  }
  .intro-copy .line { display: block; text-align: justify; text-align-last: justify; white-space: nowrap; }
  .intro-copy .line:last-child { text-align: center; text-align-last: center; }

  .promise-box {
    position: absolute; left: 440px; top: 660px; width: 318px; height: 124px;
    border: 4px solid var(--ink); text-align: center;
  }
  .promise-box .lead {
    display: block; margin-top: 10px;
    font-size: 40px; font-weight: 300; color: var(--muted); line-height: 1.1;
  }
  .promise-box .key {
    display: block; font-size: 48px; font-weight: 900; color: var(--ink); line-height: 1;
  }

  .scroll-cue { position: absolute; left: 577px; top: 824px; }
</style>
</head>
<body>
<div class="page">
  <header class="site-header">
    <a class="brand" href="#">toravi</a>
    <nav class="main-nav">
      <ul>
        <li class="nav-home is-current"><a href="#">Home</a></li>
        <li class="nav-team"><a href="#">Team</a></li>
        <li class="nav-method"><a href="#">Methodology</a></li>
        <li class="nav-areas"><a href="#">Specialist Areas</a></li>
        <li class="nav-clients"><a href="#">Clients</a></li>
        <li class="nav-candidates"><a href="#">Candidates</a></li>
        <li class="nav-group"><a href="#">Toravi group</a></li>
      </ul>
    </nav>
  </header>

  <main>
    <h1 class="intro-title">What we do?</h1>

    <div class="portrait portrait--one" role="img" aria-label="Illustrated portrait of a team member"></div>
    <div class="portrait portrait--two" role="img" aria-label="Illustrated portrait of a team member"></div>
    <div class="portrait portrait--three" role="img" aria-label="Illustrated portrait of a team member in pink accent"></div>
    <div class="portrait portrait--four" role="img" aria-label="Illustrated portrait of a team member"></div>

    <p class="intro-copy">
      <span class="line">We do recruitment based on ones belongings and purpose in life. Finding that</span>
      <span class="line">purpose in life, and just aligning ones values to correspond with the company</span>
      <span class="line">one wishes to apply. Our branding is guided by genuinely, trustworthy, helping</span>
      <span class="line">one another and making the world a better place to be in!</span>
    </p>

    <div class="promise-box">
      <span class="lead">This makes us</span>
      <strong class="key">unique.</strong>
    </div>

    <svg class="scroll-cue" width="44" height="28" viewBox="0 0 44 28" aria-label="Scroll down">
      <polyline points="3,4 22,23 41,4" fill="none" stroke="#2b2c2f" stroke-width="4" stroke-linecap="round" stroke-linejoin="round"/>
    </svg>
  </main>
</div>
</body>
</html>
```